依頼概要
第33回白鷺川大星火大会
2018年7月14日(土)午後7時30分開会
関東最大級22800発
三大花火師夢の饗宴 桐原煙火工業・宮田火工製作所・藤屋松井火工店
主催:北浜町観光協会・きたはまみなと祭り実行委員会
後援:北浜町・北浜町議会・七森町・北浜町商工会・七森町商工会・JA北陸あおば
問い合わせ:北浜町観光協会 TEL0280-81-1319
北浜町で検索的なもの
観覧チケットの購入はチケミナで検索的なもの

若干の構成を再度お願いする場合もあります。また、制作いただきました作品に、場合によりこちらで後援や開催日時等軽微な修正をする場合があります。
http://filevault-sample.jp/photo/3c1a9e07b42d58f6a0e9c2147bd86f03e5a1c9d2
上記URLは添付にあるものと同様の使用する写真です

町長様・観光協会様の方で候補作品から選んでいただきました。

ご参加・ご協力ありがとうございました。

```html
<!DOCTYPE html>
<html lang="ja">
<head>
<meta charset="utf-8">
<title>第33回白鷺川大星火大会</title>
<link rel="stylesheet" href="https://fonts.googleapis.com/css2?family=Noto+Sans+JP:wght@400;700;900&display=swap">
<style>
  :root {
    --night: #0a0f2a;
    --night-deep: #03050f;
    --burst-gold: #d9a23a;
    --burst-pink: #d8307a;
    --burst-violet: #6a3fb5;
    --white: #ffffff;
    --ink: #1a1a1a;
    --gold: #e7c45a;
    --gold-dark: #b58a20;
    --red: #d9132b;
    --pink-text: #ff3d6e;
    --footer-label: #2b2b2b;
  }
  * { box-sizing: border-box; margin: 0; padding: 0; }
  html, body { width: 849px; height: 1200px; overflow: hidden; background: var(--night-deep); }
  body { font-family: "Noto Sans JP", sans-serif; color: var(--white); }

  .poster { position: relative; width: 849px; height: 1200px; overflow: hidden; }

  .fireworks-photo {
    position: absolute; inset: 0 0 70px 0;
    background:
      radial-gradient(circle at 20% 22%, rgba(217,162,58,.55), transparent 28%),
      radial-gradient(circle at 78% 16%, rgba(106,63,181,.45), transparent 30%),
      radial-gradient(circle at 30% 62%, rgba(216,48,122,.55), transparent 30%),
      radial-gradient(circle at 70% 70%, rgba(217,162,58,.45), transparent 28%),
      radial-gradient(circle at 50% 84%, rgba(106,63,181,.4), transparent 30%),
      linear-gradient(180deg, var(--night) 0%, #1a1240 55%, var(--night-deep) 100%);
  }

  .edition {
    position: absolute; left: 325px; top: 22px; width: 283px; height: 58px;
    background: linear-gradient(180deg, var(--gold), var(--gold-dark));
    border-radius: 6px;
    color: var(--ink); font-weight: 900; font-size: 40px; line-height: 58px; text-align: center;
    letter-spacing: 2px;
  }

  .title-col {
    position: absolute; top: 92px;
    writing-mode: vertical-rl;
    font-weight: 900; font-size: 118px; line-height: 1; letter-spacing: 4px;
    text-shadow: 0 0 12px rgba(0,0,0,.6);
  }
  .title-col--river { left: 610px; top: 80px; }
  .title-col--fire  { left: 484px; }
  .title-col--meet  { left: 358px; }

  .scale-badge {
    position: absolute; left: 330px; top: 412px; width: 140px; height: 140px;
    border-radius: 50%; background: var(--red); border: 3px solid var(--white);
    display: flex; flex-direction: column; align-items: center; justify-content: center;
    font-weight: 900; line-height: 1.15;
  }
  .scale-badge .label { font-size: 20px; }
  .scale-badge .count { font-size: 24px; }

  .makers {
    position: absolute; top: 470px; right: 20px; height: 480px;
    display: flex; flex-direction: row-reverse; gap: 6px;
  }
  .makers .col {
    writing-mode: vertical-rl; font-weight: 900; line-height: 1;
    text-shadow: 0 0 8px rgba(0,0,0,.8);
  }
  .makers .headline { color: var(--pink-text); font-size: 40px; }
  .makers .maker { font-size: 38px; padding-top: 170px; }

  .event-info { position: absolute; left: 150px; top: 935px; }
  .event-date { font-weight: 900; font-size: 52px; line-height: 1; }
  .event-date small { font-size: 36px; }
  .event-date .weekday {
    display: inline-block; background: var(--white); color: var(--night);
    font-size: 30px; padding: 2px 4px; vertical-align: middle; margin-left: 2px;
  }
  .event-time { font-weight: 900; font-size: 34px; margin-top: 8px; }
  .event-venue { font-weight: 900; font-size: 50px; line-height: 1.1; margin-top: 2px; }

  .ticket-line {
    position: absolute; left: 150px; top: 1098px;
    display: flex; align-items: center; gap: 8px;
    font-size: 16px; font-weight: 700;
  }
  .search-box {
    display: inline-flex; align-items: stretch; border: 1px solid var(--white);
    font-size: 12px; background: var(--white); color: var(--ink);
  }
  .search-box span { padding: 2px 8px; }
  .search-box .button { background: #777; color: var(--white); }

  .credits {
    position: absolute; left: 0; bottom: 0; width: 849px; height: 70px;
    background: var(--white); color: var(--ink);
    padding: 6px 20px; font-size: 14px; font-weight: 700; line-height: 19px;
  }
  .credits .row { display: flex; align-items: center; gap: 8px; }
  .credits .tag {
    background: var(--footer-label); color: var(--white);
    font-size: 12px; padding: 0 6px; line-height: 17px; min-width: 48px; text-align: center;
  }
  .credits .tel { font-size: 16px; font-weight: 900; }
  .credits .town-search {
    position: absolute; right: 20px; bottom: 8px;
    background: var(--white); color: var(--ink); border: 1px solid #999;
  }
</style>
</head>
<body>
<main class="poster">
  <div class="fireworks-photo" role="img" aria-label="夜空に広がる金色・桃色・紫色の花火の写真"></div>

  <div class="edition">第33回</div>
  <h1>
    <span class="title-col title-col--river">白鷺川</span>
    <span class="title-col title-col--fire">大星火</span>
    <span class="title-col title-col--meet">大会</span>
  </h1>

  <div class="scale-badge">
    <span class="label">関東最大級</span>
    <span class="count">22800発</span>
  </div>

  <div class="makers">
    <div class="col headline">三大花火師夢の饗宴</div>
    <div class="col maker">★桐原煙火工業</div>
    <div class="col maker">★宮田火工製作所</div>
    <div class="col maker">★藤屋松井火工店</div>
  </div>

  <section class="event-info">
    <p class="event-date">2018<small>年</small>7<small>月</small>14<small>日</small><span class="weekday">土</span></p>
    <p class="event-time">午後7時30分開会</p>
    <p class="event-venue">北浜町白鷺川河川敷</p>
  </section>

  <p class="ticket-line">
    観覧チケットの購入はチケミナで検索
    <span class="search-box"><span>白鷺川大星火大会</span><span class="button">検索</span></span>
  </p>

  <footer class="credits">
    <div class="row"><span class="tag">主催</span>北浜町観光協会・きたはまみなと祭り実行委員会</div>
    <div class="row"><span class="tag">後援</span>北浜町・北浜町議会・七森町・北浜町商工会・七森町商工会・JA北陸あおば</div>
    <div class="row"><span class="tag">問い合わせ</span>北浜町観光協会 <span class="tel">TEL 0290-64-7725</span></div>
    <span class="search-box town-search"><span>北浜町</span><span class="button">検索</span></span>
  </footer>
</main>
</body>
</html>
```